Merrivale construction website for a high end luxury custom home builder

I need a website designed for a high end luxury custom home builder. I would like the website to host a number activities. A blog/vlog on the page where I can post about the projects being built how to's what to look out for during the build, A designated testimonial page but also having testimonials posted on the other pages like the gallery linked to the photos of the completed projects. a gallery page, an about us page, services page that demonstrate what we do and what we are capable of, and hopefully when I start winning awards, and awards page.
Home page
about us page
services page
gallery
testimonial
awards page but I my need to add that later.
I already have the domain name for the website. www.merrivaleconstruction.com.au
I recently completed a sketch hive page for my logo and will post the logo documents below.

Target Market(s)

I'd like to target professions with cash enough to build a house. I would like peolpe to understand that they are buy a price when they are getting quote to build there house. It seems like people just look for the cheapest price and end up with an inferior product. Where as people need to understand that a builder with the high price ( not astronomically higher 15-20% higher) are the ones with correct systems in place, a bide by correct OHS and use proper and correct product. If that can be conveyed through the website somehow, without saying it directly, it would be awesome.

Font styles to use
Sans Serif

Requirements
Must have
• I would like the testimonials to have a designated page (mentioned in the brief) but I would like the testimonials to be linked to the gallery page and when the picture are open of completed job the relevant testimonials would pop up near the pictures.

Nice to have
• I would like peolpe to understand that they are buy a price when they are getting quote to build there house. It seems like people just look for the cheapest price and end up with an inferior product. Where as people need to understand that a builder with the high price ( not astronomically higher 15-20% higher) are the ones with correct systems in place, a bide by correct OHS and use proper and correct product. If that can be conveyed through the website somehow, without saying it directly, it would be awesome.

```html
<!DOCTYPE html>
<html lang="en">
<head>
<meta charset="utf-8">
<title>Merrivale Construction</title>
<link href="https://fonts.googleapis.com/css2?family=Poppins:wght@400;500;600;700;800&display=swap" rel="stylesheet">
<style>
:root{
  --blue:#2a7cc7;
  --blue-dark:#1f66a8;
  --ink:#2f2f2f;
  --muted:#777;
  --bar:#4d4d4d;
  --white:#fff;
  --line:#e3e3e3;
}
*{box-sizing:border-box;margin:0;padding:0}
html,body{width:1200px;height:4751px;overflow:hidden}
body{font-family:'Poppins',sans-serif;color:var(--ink);background:var(--white);position:relative}
.abs{position:absolute}
.btn{position:absolute;background:var(--blue);color:var(--white);font-weight:600;font-size:14px;display:flex;align-items:center;justify-content:center;text-transform:uppercase;border-radius:2px}
.section-title{font-weight:800;font-size:34px;text-transform:uppercase;letter-spacing:.5px}
.section-title span{color:var(--blue)}
.photo{position:absolute}

/* top bar */
.topbar{top:0;left:0;width:1200px;height:30px;background:var(--bar);color:var(--white);font-size:13px}
.topbar .contact{position:absolute;left:65px;top:6px;display:flex;gap:34px;align-items:center}
.topbar .contact span{display:flex;gap:10px;align-items:center}
.topbar .social{position:absolute;right:62px;top:8px;display:flex;gap:15px}
.topbar .social i{display:block;width:15px;height:15px;background:var(--white);border-radius:2px}

/* header */
.header{top:30px;left:0;width:1200px;height:103px;background:var(--white)}
.brand{position:absolute;display:flex;align-items:center;gap:10px;color:var(--blue);font-weight:600;text-transform:uppercase}
.brand .mark{background:var(--blue);flex:none}
.header .brand{left:86px;top:28px;font-size:21px}
.header .brand .mark{width:40px;height:46px}
.nav{position:absolute;right:88px;top:40px;display:flex;gap:35px;font-size:15px;font-weight:500}
.nav .active{color:var(--blue)}

/* hero */
.hero{top:133px;left:0;width:1200px;height:615px;background:linear-gradient(180deg,#5fa5df 0%,#9cc8ea 30%,#7b8a7a 55%,#4f6a3b 80%,#3f5a2c 100%)}
.hero h1{position:absolute;left:66px;top:235px;color:var(--white);font-size:58px;font-weight:800;line-height:70px;text-transform:uppercase;letter-spacing:.5px}
.hero .btn{left:66px;top:401px;width:170px;height:38px}
.dots{position:absolute;left:550px;top:555px;display:flex;gap:17px}
.dots i{width:22px;height:5px;background:var(--white)}
.dots i+i{background:var(--blue)}

/* about */
.about-title{left:65px;top:828px}
.about-text{left:65px;top:882px;width:610px;font-size:13px;line-height:30px;color:#555}
.about-photo{left:686px;top:870px;width:448px;height:297px;border:3px solid var(--blue);border-radius:6px;background:linear-gradient(180deg,#8fc1ea,#e8eef2 45%,#7fc8d8 75%,#c9c9c2)}
.about .btn{left:66px;top:1124px;width:151px;height:43px}

.listing{position:absolute;top:1253px;width:336px}
.listing .frame{height:286px;border:6px solid #eee;border-radius:10px;box-shadow:0 1px 4px rgba(0,0,0,.15)}
.listing .price{margin-top:30px;text-align:center;color:var(--blue);font-weight:600;font-size:16px}
.listing .place{margin-top:14px;text-align:center;color:var(--muted);font-size:14px;line-height:18px}
.view-all{width:152px;height:38px}

/* services */
.services{top:1834px;left:0;width:1200px;height:475px;background:linear-gradient(90deg,#6b8fb0,#93a6b5 60%,#6f8a55)}
.services .panel{position:absolute;left:0;top:0;width:772px;height:475px;background:rgba(42,124,199,.78)}
.services .section-title{position:absolute;left:64px;top:46px;color:var(--white)}
.service{position:absolute;width:300px;color:var(--white)}
.service svg{display:block;margin-bottom:8px}
.service h3{font-size:17px;font-weight:600}
.service p{font-size:13px;line-height:17px;margin-top:6px}

/* gallery */
.gallery-title{left:0;width:1200px;top:2388px;text-align:center}
.tile{position:absolute}

/* testimonial */
.testimonial{top:3216px;left:0;width:1200px;height:546px;background:linear-gradient(180deg,#3d8fd6,#7fb3dc 40%,#6b8b9a 70%,#55704a)}
.testimonial .section-title{position:absolute;top:28px;width:1200px;text-align:center;color:var(--white)}
.t-photo{left:142px;top:108px;width:352px;height:350px;background:linear-gradient(180deg,#f2f2f2,#d9dde2);border:1px solid #ddd}
.t-card{position:absolute;left:462px;top:234px;width:598px;height:251px;background:var(--white);border-left:9px solid var(--blue);text-align:center;padding:50px 40px}
.t-card h4{font-size:16px;font-weight:600;text-transform:uppercase}
.t-card p{margin-top:30px;font-size:13px;line-height:25px;color:#555}
.arrow{position:absolute;width:40px;height:40px;display:flex;align-items:center;justify-content:center}
.quote{position:absolute;color:var(--white);font-size:72px;font-weight:800;line-height:1}

/* awards */
.awards-title{left:0;width:1200px;top:3842px;text-align:center}
.award{position:absolute;top:3903px;width:303px;text-align:center}
.award .card{height:332px;border:4px solid #f0f0f0;border-radius:10px;box-shadow:0 1px 5px rgba(0,0,0,.12);position:relative}
.award .card div{position:absolute;left:90px;top:25px;width:115px;height:285px;background:linear-gradient(180deg,#f2c14a,#c28b1e 70%,#5a2a16)}
.award .year{margin-top:16px;color:var(--blue);font-size:21px;font-weight:600}
.award .label{margin-top:2px;font-size:17px;font-weight:500}

/* footer */
.footer .brand{left:65px;top:4475px;font-size:26px;line-height:32px;gap:16px;width:330px}
.footer .brand .mark{width:60px;height:90px}
.footer .brand .name{display:block}
.fcol{position:absolute;top:4415px;font-size:15px;font-weight:500}
.fcol h5{color:var(--blue);font-size:16px;font-weight:600;text-transform:uppercase;margin-bottom:16px}
.fcol li{list-style:none;line-height:38px}
.fcol .row{display:flex;align-items:center;gap:14px;line-height:36px;white-space:nowrap}
.fsocial{display:flex;gap:26px;margin-top:24px}
.fsocial i{display:block;width:24px;height:24px;border:2px solid var(--blue);border-radius:3px}
.news{position:absolute;left:830px;top:4448px;display:flex}
.news .field{width:191px;height:47px;border:1px solid #ccc;font-size:12px;color:#999;padding:14px 10px}
.news .sub{width:113px;height:47px;background:var(--blue);color:var(--white);font-size:13px;font-weight:600;display:flex;align-items:center;justify-content:center}
.rule{left:65px;top:4685px;width:1069px;height:1px;background:#999}
.copy{left:0;width:1200px;top:4703px;text-align:center;font-size:15px;color:#555}
</style>
</head>
<body>

<div class="abs topbar">
  <div class="contact">
    <span><svg width="12" height="12" viewBox="0 0 24 24"><path fill="#fff" d="M6.6 10.8a15 15 0 0 0 6.6 6.6l2.2-2.2c.3-.3.7-.4 1-.2 1.1.4 2.3.6 3.6.6.6 0 1 .4 1 1V20c0 .6-.4 1-1 1A17 17 0 0 1 3 4c0-.6.4-1 1-1h3.5c.6 0 1 .4 1 1 0 1.3.2 2.5.6 3.6.1.3 0 .7-.2 1z"/></svg>+945 555 0142</span>
    <span><svg width="13" height="10" viewBox="0 0 24 18"><path fill="#fff" d="M0 0h24v2L12 10 0 2zM0 4l12 8 12-8v14H0z"/></svg>hello@merrivalemail.com</span>
  </div>
  <div class="social"><i></i><i></i><i></i><i></i><i></i></div>
</div>

<header class="abs header">
  <div class="brand"><i class="mark"></i>Merrivale Construction</div>
  <nav class="nav"><span class="active">Home</span><span>About us</span><span>Services</span><span>Gallery</span><span>Blog</span><span>Contact us</span></nav>
</header>

<section class="abs hero" role="img" aria-label="Large two-storey timber family home with a double garage, surrounded by pine trees under a blue sky">
  <h1>Welcome to<br>Merrivale Construction</h1>
  <div class="btn">Contact now</div>
  <div class="dots"><i></i><i></i><i></i></div>
</section>

<section class="about">
  <h2 class="abs section-title about-title">About <span>Merrivale</span></h2>
  <p class="abs about-text">It is a long established fact that a reader will be distracted by the readable content of a page when looking at its layout. The point of using Lorem Ipsum is that it has a more-or-less normal distribution of letters, as opposed to using 'Content here, content here', making it look like readable English. It is a long established fact that a reader will be distracted by the readable content of a page when looking at its layout. The point of using Lorem Ipsum is that it has a more-or-less normal distribution of letters,</p>
  <div class="photo about-photo" role="img" aria-label="Modern white villa with a curved swimming pool and outdoor dining terrace"></div>
  <div class="btn">Read now</div>

  <div class="listing" style="left:60px">
    <div class="frame" role="img" aria-label="Luxury home with pool, sun loungers and a red-tiled pavilion" style="background:linear-gradient(180deg,#8ec3ee,#f1ebe2 50%,#9bc9d8 75%,#8d8a85)"></div>
    <div class="price">$10,900,000 USD</div>
    <div class="place">Scottsdale, AZ, United States</div>
  </div>
  <div class="listing" style="left:430px">
    <div class="frame" role="img" aria-label="Dark A-frame house among tall pine trees" style="background:linear-gradient(180deg,#5d5a4d,#3a3a36 50%,#6d5a44)"></div>
    <div class="price">$2,495,000 CAD</div>
    <div class="place">Côte Des Neiges/Notre Dame<br>De Grâce (Montréal), QC, Canada</div>
  </div>
  <div class="listing" style="left:802px">
    <div class="frame" role="img" aria-label="Contemporary two-storey home with a green lawn and stepping stones" style="background:linear-gradient(180deg,#6fb0ea,#c8d4dc 50%,#6f9a45)"></div>
    <div class="price">$4,695,000 USD</div>
    <div class="place">Watersound, FL, United States</div>
  </div>
  <div class="btn view-all" style="left:523px;top:1708px">View all</div>
</section>

<section class="abs services" role="img" aria-label="Stone house with a wooden garage door beside a leafy tree">
  <div class="panel"></div>
  <h2 class="section-title">Services</h2>
  <div class="service" style="left:100px;top:122px">
    <svg width="40" height="40" viewBox="0 0 40 40"><circle cx="20" cy="20" r="17" fill="none" stroke="#fff" stroke-width="2"/><path d="M20 9c4 6 7 9 7 13a7 7 0 0 1-14 0c0-4 3-7 7-13z" fill="#fff"/></svg>
    <h3>Awesome Amenities</h3>
    <p>It is a long established fact that a reader will be distracted by the readable content of a page when looking at its layout.</p>
  </div>
  <div class="service" style="left:423px;top:122px">
    <svg width="40" height="40" viewBox="0 0 40 40"><path d="M20 8a9 9 0 0 0-5 16v4h10v-4a9 9 0 0 0-5-16zM16 31h8v3h-8z" fill="none" stroke="#fff" stroke-width="2"/></svg>
    <h3>Power and Energy</h3>
    <p>It is a long established fact that a reader will be distracted by the readable content of a page when looking at its layout.</p>
  </div>
  <div class="service" style="left:100px;top:294px">
    <svg width="40" height="40" viewBox="0 0 40 40"><circle cx="20" cy="20" r="15" fill="none" stroke="#fff" stroke-width="2"/><text x="20" y="25" font-size="12" font-family="Poppins,sans-serif" font-weight="600" fill="#fff" text-anchor="middle">24</text></svg>
    <h3>24 Hours Service</h3>
    <p>It is a long established fact that a reader will be distracted by the readable content of a page when looking at its layout.</p>
  </div>
  <div class="service" style="left:423px;top:294px">
    <svg width="40" height="40" viewBox="0 0 40 40"><circle cx="20" cy="14" r="7" fill="none" stroke="#fff" stroke-width="2"/><path d="M7 34c1-8 6-11 13-11s12 3 13 11z" fill="none" stroke="#fff" stroke-width="2"/></svg>
    <h3>Good Neighbourhood</h3>
    <p>It is a long established fact that a reader will be distracted by the readable content of a page when looking at its layout.</p>
  </div>
</section>

<section class="gallery">
  <h2 class="abs section-title gallery-title">Photo <span>Gallery</span></h2>
  <div class="tile" role="img" aria-label="Tudor-style house on a green lawn" style="left:65px;top:2453px;width:362px;height:275px;background:linear-gradient(180deg,#7fb6e6,#dce8ef 45%,#5b6a45 70%,#5f8a3a)"></div>
  <div class="tile" role="img" aria-label="Living room with a patterned ceiling, shown with a view overlay" style="left:440px;top:2453px;width:297px;height:275px;background:linear-gradient(180deg,#4d8ecb,#3b79b8)">
    <svg class="abs" style="left:128px;top:122px" width="40" height="30" viewBox="0 0 40 30"><path d="M2 15C8 5 32 5 38 15 32 25 8 25 2 15z" fill="#fff"/><circle cx="20" cy="15" r="6" fill="#3b79b8"/></svg>
  </div>
  <div class="tile" role="img" aria-label="Bright bedroom with a wooden bed opening onto a garden" style="left:750px;top:2453px;width:384px;height:275px;background:linear-gradient(90deg,#e9e3da,#f6f4f0 50%,#6f9e52)"></div>
  <div class="tile" role="img" aria-label="White house entrance with garden hedges" style="left:65px;top:2742px;width:298px;height:275px;background:linear-gradient(180deg,#b9c7d4,#e8e4dc 50%,#7c7c78)"></div>
  <div class="tile" role="img" aria-label="Poolside dining table beside a modern house" style="left:376px;top:2742px;width:383px;height:275px;background:linear-gradient(180deg,#e9e5de,#d4d0c8 55%,#7e8da0)"></div>
  <div class="tile" role="img" aria-label="Modern three-storey house lit at dusk" style="left:773px;top:2742px;width:361px;height:275px;background:linear-gradient(180deg,#3e4a6a,#5c5560 55%,#6b4a3a)"></div>
  <div class="btn view-all" style="left:518px;top:3087px;width:165px;height:41px">View all</div>
</section>

<section class="abs testimonial" role="img" aria-label="Faded backdrop of a family house under a blue sky">
  <h2 class="section-title">Testimonial</h2>
  <div class="photo t-photo" role="img" aria-label="Portrait of a smiling client in a shirt and tie"></div>
  <div class="t-card">
    <h4>Elena R. Hale</h4>
    <p>It is a long established fact that a reader will be distracted by the readable content of a page when looking at its layout. The point of using Lorem Ipsum is that it has a more-or-less normal distribution of letters, as opposed to using 'Content here, content here', making it look like readable English.</p>
  </div>
  <div class="arrow" style="left:1015px;top:234px;background:var(--blue)"><svg width="14" height="16" viewBox="0 0 14 16"><path d="M10 2 4 8l6 6" fill="none" stroke="#fff" stroke-width="3"/></svg></div>
  <div class="arrow" style="left:1060px;top:194px;background:var(--blue)"><svg width="14" height="16" viewBox="0 0 14 16"><path d="m4 2 6 6-6 6" fill="none" stroke="#fff" stroke-width="3"/></svg></div>
  <div class="quote" style="left:943px;top:98px;font-size:52px">”</div>
  <div class="quote" style="left:1062px;top:80px">”</div>
</section>

<section class="awards">
  <h2 class="abs section-title awards-title"><span>Awards</span></h2>
  <div class="award" style="left:94px"><div class="card" role="img" aria-label="Gold trophy cup on a black base"><div></div></div><div class="year">2018</div><div class="label">Awards 1</div></div>
  <div class="award" style="left:447px"><div class="card" role="img" aria-label="Gold spiral award statuette"><div style="left:120px;width:60px"></div></div><div class="year">2019</div><div class="label">Awards 2</div></div>
  <div class="award" style="left:801px"><div class="card" role="img" aria-label="Gold abstract figure award"><div style="left:115px;width:70px"></div></div><div class="year">2020</div><div class="label">Awards 3</div></div>
</section>

<footer class="footer">
  <div class="brand"><i class="mark"></i><span><span class="name">Merrivale</span><span class="name">Construction</span></span></div>
  <div class="fcol" style="left:418px">
    <h5>Links</h5>
    <ul><li>Home</li><li>About us</li><li>Services</li><li>Gallery</li><li>Blog</li><li>Contact us</li></ul>
  </div>
  <div class="fcol" style="left:584px">
    <h5>Contact us</h5>
    <div class="row"><svg width="16" height="16" viewBox="0 0 24 24"><path fill="#2a7cc7" d="M6.6 10.8a15 15 0 0 0 6.6 6.6l2.2-2.2c.3-.3.7-.4 1-.2 1.1.4 2.3.6 3.6.6.6 0 1 .4 1 1V20c0 .6-.4 1-1 1A17 17 0 0 1 3 4c0-.6.4-1 1-1h3.5c.6 0 1 .4 1 1 0 1.3.2 2.5.6 3.6.1.3 0 .7-.2 1z"/></svg>+945 555 0142</div>
    <div class="row"><svg width="16" height="12" viewBox="0 0 24 18"><path fill="#2a7cc7" d="M0 0h24v2L12 10 0 2zM0 4l12 8 12-8v14H0z"/></svg>hello@merrivalemail.com</div>
    <div class="fsocial"><i></i><i></i><i></i><i></i><i></i></div>
  </div>
  <div class="fcol" style="left:830px"><h5>Submit newsletters</h5></div>
  <div class="news"><div class="field">YOUR EMAIL</div><div class="sub">SUBSCRIBE</div></div>
  <div class="abs rule"></div>
  <p class="abs copy">Copyright © Companyname 2020.All right reserved.</p>
</footer>

</body>
</html>
```